Taco Food Wagon WRAP OR LABELS

We are looking for a food wagon wrap design that is bold and classy, see pictures attached. Our company is selling the best and cheapest fast food Taco in Iceland and the name is "Bita Kofinn". The wagon is used for private parties, companies service and night sale in Iceland.

We need something bold and rememberable. Many thanks

Target Market(s)

Hungry folks

Industry/Entity Type

Food Truck

Logo Text

Bita Kofinn

Colors

Designer to choose colors to be used in the design.

Requirements
Nice to have
• figurative

```html
<!DOCTYPE html>
<html lang="en">
<head>
<meta charset="utf-8">
<title>Bita Kofinn – Food Wagon Wrap</title>
<link rel="stylesheet" href="https://fonts.googleapis.com/css2?family=Bebas+Neue&family=Josefin+Sans:wght@400;600&display=swap">
<style>
  :root {
    --paper: #ffffff;
    --maroon: #7e1310;
    --sand: #f4d4ae;
    --cream: #f5e5d3;
    --orange: #f45315;
    --taco: #fd740d;
    --taco-deep: #e0600b;
  }
  html, body {
    margin: 0;
    width: 1186px;
    height: 1200px;
    overflow: hidden;
    background: var(--paper);
  }
  .sheet {
    position: relative;
    width: 1186px;
    height: 1200px;
  }
  .side-label {
    position: absolute;
    left: 0;
    width: 1186px;
    margin: 0;
    text-align: center;
    font-family: "Bebas Neue", sans-serif;
    font-weight: 400;
    font-size: 44px;
    letter-spacing: 36px;
    text-indent: 36px;
    color: var(--maroon);
    line-height: 1;
  }
  .side-label--front { top: 68px; }
  .side-label--back { top: 706px; }
  .card {
    position: absolute;
    left: 225px;
    display: block;
  }
  .card--front { top: 162px; }
  .card--back { top: 802px; }
  .tagline { font-family: "Josefin Sans", sans-serif; font-weight: 600; font-size: 13px; letter-spacing: 2px; fill: var(--maroon); }
  .tagline-flagword { font-family: "Josefin Sans", sans-serif; font-weight: 400; font-size: 20px; letter-spacing: 2px; fill: var(--cream); }
  .brand-name { font-family: "Bebas Neue", sans-serif; fill: var(--maroon); }
  .slogan { font-family: "Bebas Neue", sans-serif; fill: var(--cream); }
</style>
</head>
<body>
<main class="sheet">
  <h2 class="side-label side-label--front">Front</h2>

  <svg class="card card--front" width="730" height="416" viewBox="0 0 730 416" aria-label="Wagon wrap, front side">
    <defs>
      <clipPath id="front-clip"><rect width="730" height="416"/></clipPath>
      <linearGradient id="taco-tone-front" x1="0" y1="0" x2="0" y2="1">
        <stop offset="0" stop-color="var(--taco)"/>
        <stop offset="1" stop-color="var(--taco-deep)"/>
      </linearGradient>
    </defs>
    <g clip-path="url(#front-clip)">
      <rect class="card-bg" width="730" height="416" fill="var(--sand)"/>
      <rect class="taco-art" role="img" aria-label="Illustration of two tacos with tomato and lettuce filling"
            x="333" y="298" width="397" height="118" rx="18" fill="url(#taco-tone-front)"/>
      <path class="dark-field" d="M0,42 C90,260 330,380 600,416 L0,416 Z" fill="var(--maroon)"/>
      <path class="edge-band" d="M6,0 C80,230 330,372 730,410" fill="none" stroke="var(--cream)" stroke-width="12"/>

      <g class="tagline-row">
        <line x1="132" y1="0" x2="132" y2="13" stroke="var(--orange)" stroke-width="1.5"/>
        <line x1="337" y1="0" x2="337" y2="13" stroke="var(--orange)" stroke-width="1.5"/>
        <path d="M91,12 L178,12 L172,24.5 L178,37 L91,37 L97,24.5 Z" fill="var(--orange)"/>
        <path d="M256,12 L420,12 L414,24.5 L420,37 L256,37 L262,24.5 Z" fill="var(--orange)"/>
        <text class="tagline" x="58" y="31">THE</text>
        <text class="tagline-flagword" x="135" y="32" text-anchor="middle">BEST</text>
        <text class="tagline" x="181" y="31">AND THE</text>
        <text class="tagline-flagword" x="338" y="32" text-anchor="middle">CHEAPEST</text>
        <text class="tagline" x="423" y="31">FAST FOOD TACO IN ICELAND</text>
      </g>

      <g class="brand">
        <text class="brand-name" x="365" y="200" text-anchor="middle" font-size="72">BITA</text>
        <text class="brand-name" x="365" y="262" text-anchor="middle" font-size="72">KOFINN</text>
      </g>
    </g>
  </svg>

  <h2 class="side-label side-label--back">Back</h2>

  <svg class="card card--back" width="730" height="343" viewBox="0 0 730 343" aria-label="Wagon wrap, back side">
    <defs>
      <clipPath id="back-clip"><rect width="730" height="343"/></clipPath>
      <linearGradient id="taco-tone-back" x1="0" y1="0" x2="0" y2="1">
        <stop offset="0" stop-color="var(--taco)"/>
        <stop offset="1" stop-color="var(--taco-deep)"/>
      </linearGradient>
      <linearGradient id="split-fill" x1="0" y1="0" x2="0" y2="1">
        <stop offset="0.55" stop-color="var(--cream)"/>
        <stop offset="0.55" stop-color="var(--orange)"/>
      </linearGradient>
    </defs>
    <g clip-path="url(#back-clip)">
      <rect class="card-bg" width="730" height="343" fill="var(--sand)"/>
      <rect class="taco-art" role="img" aria-label="Close-up illustration of a taco with tomato and lettuce filling"
            x="340" y="204" width="390" height="160" rx="24" fill="url(#taco-tone-back)"/>
      <path class="dark-field" d="M0,0 L316,0 C352,110 352,230 302,343 L0,343 Z" fill="var(--maroon)"/>
      <path class="edge-band" d="M324,-4 C366,110 366,232 310,348" fill="none" stroke="var(--cream)" stroke-width="18"/>

      <g class="slogan-block">
        <text class="slogan" x="162" y="116" text-anchor="middle" font-size="92" letter-spacing="3" fill="url(#split-fill)">THE BEST</text>
        <text class="slogan" x="169" y="178" text-anchor="middle" font-size="62" letter-spacing="2">THE CHEAPEST</text>
        <text class="slogan" x="168" y="231" text-anchor="middle" font-size="42" letter-spacing="2">FAST FOOD TACO</text>
        <text class="slogan" x="160" y="277" text-anchor="middle" font-size="42" letter-spacing="2">IN ICELAND</text>
      </g>

      <g class="brand">
        <text class="brand-name" x="550" y="100" text-anchor="middle" font-size="104">BITA</text>
        <text class="brand-name" x="550" y="190" text-anchor="middle" font-size="104">KOFINN</text>
      </g>
    </g>
  </svg>
</main>
</body>
</html>
```